Company brochure for our unique consulting business

We are a small consulting business offering a unique set of services to our clients.. In simple terms we are a business improvement consultancy helping our clients get the best out of their businesses. We work with clients across multiple sectors and deliver a variety of services. We want to put together a brochure to cover these main themes:1. Who we are2. What we do3. The type of people we employ4. The sectors we work inWhile the brochure needs to have a certain corporate feel to it, we don't want it to be "boring" or "stiff". We would like it to have a slightly "friendly" or "informal" feel to it, to reflect the type of organisation we are.We have a company website http://tollandvergeadvisory.com , however we do not want to directly replicate the content or feel as we recognise it needs updating.We would like the brochure to be A4 portrait format. We anticipate requiring 12 sides (including covers) but we are happy to be guided on this based on the content we have provided.The attached ppt file gives the detail of the content to be included and also shows the proposed pagination. For the front cover we would like to try 2 versions, one with the TVA logo and one with the Tolland Verge Advisory logo (a file of both is attached)One of the most important pages will be the "Our Services" page. We would like this to cover the centre fold. In the ppt file we have shown an example layout, but this is where we need most help - we are clearly not graphic designers! This page will be the most used page in sales meetings etc.Also attached is the following:1. file for our TollandVerge Advisory company logo.2. File for our TVA company logo3. Files for Derek's signatures (for under photos) - Owen's to follow4. Photo of Derek & Owen (person in purple shirt to be cropped out)Thank you and really excited to see what everyone comes back with.Derek & Owen

Target Market(s)

Very broad - Manufacturing, Healthcare, Hospitality

Industry/Entity Type

Management Consulting

Font styles to use
Other font styles liked:
• We use Swiss721, but happy to be guided by designer

Colors
3276b5
85abd2
0355a3
333333
5c5c5c
9d9d9d
d9d9d9

Requirements
Must have
• Corporate feel
Nice to have
• Slightly friendly feel
• Our standard "blue" is (CORRECTION) - R55 G96 B146 #376092 and our standard grey is R197 G178, B179 - #B3B2B2, which we would like to keep, but other colours we are happy to be guided on. Brand guidelines attached.

```html
<!DOCTYPE html>
<html lang="en">
<head>
<meta charset="utf-8">
<title>TVA Quotes</title>
<link rel="stylesheet" href="https://fonts.googleapis.com/css2?family=Arimo:wght@700&family=Open+Sans:ital,wght@1,400&display=swap">
<style>
  :root {
    --brand-blue: #1f4fc0;
    --header-deep: #2346c9;
    --header-light: #6fa3ef;
    --rule-dark: #3c4a52;
    --quote-grey: #6b7a80;
    --ink: #111111;
    --panel-grey: #c8d3d6;
    --band-blue: #2c4fb0;
    --white: #ffffff;
  }
  * { margin: 0; padding: 0; box-sizing: border-box; }
  html, body { width: 848px; height: 1200px; overflow: hidden; background: var(--white); }
  .page { position: relative; width: 848px; height: 1200px; overflow: hidden; font-family: "Open Sans", Arial, sans-serif; }

  .page-header {
    position: absolute; left: 0; top: 0; width: 848px; height: 124px;
    background: linear-gradient(90deg, var(--header-deep) 0%, #3566e0 55%, var(--header-light) 100%);
  }
  .header-rule { position: absolute; left: 0; top: 124px; width: 848px; height: 8px; background: var(--rule-dark); }
  .page-title {
    position: absolute; right: 80px; top: 68px;
    font-family: "Arimo", Arial, sans-serif; font-weight: 700; font-size: 32px;
    color: var(--white); line-height: 1;
  }

  .quote-mark { position: absolute; font-family: Georgia, serif; font-weight: 700; line-height: 1; }
  .quote-mark--lead { left: 140px; top: 226px; font-size: 118px; color: var(--brand-blue); }
  .quote-mark--small { font-size: 64px; color: var(--quote-grey); }

  .quote { position: absolute; text-align: center; font-style: italic; }
  .quote-text { color: var(--ink); font-size: 14px; line-height: 23px; }
  .quote-source { color: var(--brand-blue); font-size: 15px; line-height: 18px; margin-top: 21px; }

  .quote--lead { left: 229px; width: 400px; top: 295px; }
  .quote--lead .quote-text { color: var(--brand-blue); font-size: 20.5px; line-height: 28.5px; }
  .quote--lead .quote-source { color: var(--ink); font-size: 17px; line-height: 20px; margin-top: 22px; }

  .footer-panel { position: absolute; left: 0; top: 0; }
  .page-number { position: absolute; left: 789px; top: 1135px; font-family: "Arimo", Arial, sans-serif; font-size: 20px; color: var(--ink); }
</style>
</head>
<body>
<main class="page">
  <div class="page-header" role="img" aria-label="City skyline photograph in blue tones"></div>
  <div class="header-rule"></div>
  <h1 class="page-title">TVA Quotes</h1>

  <span class="quote-mark quote-mark--lead">&ldquo;</span>
  <figure class="quote quote--lead">
    <p class="quote-text">TVA have achieved excellent engagement<br>throughout the entire organisation with<br>significant measurable successes.&rdquo;</p>
    <p class="quote-source">Director of Operations<br>Halvern Security</p>
  </figure>

  <span class="quote-mark quote-mark--small" style="left:56px;top:592px">&ldquo;</span>
  <figure class="quote" style="left:80px;width:320px;top:614px">
    <p class="quote-text">With the team from TVA we have been able<br>to embed an improvement approach across<br>the entire organisation. &ldquo;</p>
    <p class="quote-source" style="margin-left:-20px">Chief Operations Officer<br>Westbrook Hospital</p>
  </figure>

  <span class="quote-mark quote-mark--small" style="left:432px;top:594px">&ldquo;</span>
  <figure class="quote" style="left:448px;width:320px;top:610px">
    <p class="quote-text">You have definitely made our lives easier<br>knowing that you are taking care of our<br>British colleagues.&nbsp; If we have future needs,<br>we will definitely be straight back to you.&rdquo;</p>
    <p class="quote-source" style="margin-left:-12px">Chief Operations Officer<br>Northgate Games</p>
  </figure>

  <span class="quote-mark quote-mark--small" style="left:60px;top:790px">&ldquo;</span>
  <figure class="quote" style="left:76px;width:320px;top:810px">
    <p class="quote-text">The team from TVA have been invaluable<br>with helping implement our lean<br>programme.&nbsp; They&rsquo;ve helped break down<br>what seemed very complicated at the start,<br>into logical and simple steps. &ldquo;</p>
    <p class="quote-source" style="margin-left:-12px">Managing Director<br>Penmark Supplies</p>
  </figure>

  <span class="quote-mark quote-mark--small" style="left:444px;top:792px">&ldquo;</span>
  <figure class="quote" style="left:446px;width:320px;top:812px">
    <p class="quote-text">TVA have been able offer us support<br>across a range of topics based on their<br>in-depth knowledge of lean and Kessler<br>systems. &ldquo;</p>
    <p class="quote-source" style="margin-top:36px">Continuous Improvement Manager<br>Corvane Motors</p>
  </figure>

  <svg class="footer-panel" width="848" height="1200" viewBox="0 0 848 1200" aria-hidden="true">
    <defs>
      <linearGradient id="band-fill" x1="0" y1="0" x2="0" y2="1">
        <stop offset="0" stop-color="#1e3f9e"/>
        <stop offset="0.3" stop-color="var(--band-blue)"/>
        <stop offset="1" stop-color="#3459c0"/>
      </linearGradient>
    </defs>
    <polygon points="848,936 716,1200 848,1200" fill="var(--panel-grey)"/>
    <polygon points="0,1122 764,1122 722,1200 0,1200" fill="url(#band-fill)"/>
    <polygon points="788,1166 848,1166 848,1182 774,1182" fill="#4f5b60"/>
  </svg>
  <span class="page-number">5</span>
</main>
</body>
</html>
```